Chiropractic Auto Accident Billboard

Billboard for Auto Accident Chiropractor
Kestrelwood Rehab
(770) 48-SPINE
Habla Espanol
Same Day Appointments - Locations across Georgia
INJURED IN A CAR ACCIDENT?

Target Market(s)

People in Auto Accidents

Industry/Entity Type

Personal Injury

Requirements
Must have
• BIG PHONE Number

```html
<!DOCTYPE html>
<html lang="en">
<head>
<meta charset="UTF-8">
<title>Kestrelwood Rehab – Auto Accident Billboard</title>
<link href="https://fonts.googleapis.com/css2?family=Poppins:wght@500;600;700;800&display=swap" rel="stylesheet">
<style>
  :root {
    --page-bg: #ffffff;
    --board-black: #0b0b0b;
    --brand-green: #3e9140;
    --brand-green-dark: #2f7a33;
    --ink: #111111;
    --white: #ffffff;
    --orange-light: #f7c55a;
    --orange-deep: #ea7a1c;
  }
  * { margin: 0; padding: 0; box-sizing: border-box; }
  html, body {
    width: 1089px; height: 1200px; overflow: hidden;
    background: var(--page-bg);
    font-family: 'Poppins', sans-serif;
  }
  .billboard {
    position: absolute; left: 44px; top: 454px;
    width: 1000px; height: 292px;
    background: var(--white);
    box-shadow: 0 10px 22px rgba(0,0,0,0.28);
    overflow: hidden;
  }
  .headline-panel {
    position: absolute; left: 0; top: 0; width: 1000px; height: 196px;
    background: var(--board-black);
  }
  .portrait-area {
    position: absolute; left: 660px; top: 0; width: 340px; height: 196px;
    background:
      radial-gradient(ellipse at 85% 45%, rgba(230,80,20,0.85) 0%, rgba(140,30,10,0.6) 25%, rgba(40,10,8,0) 55%),
      linear-gradient(90deg, #0b0b0b 0%, #2a2624 35%, #3a1a12 70%, #241210 100%);
  }
  .headline {
    position: absolute; left: 21px; top: 14px;
    font-weight: 700; line-height: 1; text-transform: uppercase;
  }
  .headline-lead {
    display: block; color: var(--white);
    font-size: 54px; letter-spacing: -0.5px;
  }
  .headline-main {
    display: block; margin-top: 2px;
    font-size: 77px; font-weight: 800; letter-spacing: -1px;
    background: linear-gradient(180deg, var(--orange-deep) 0%, var(--orange-light) 55%, var(--orange-deep) 100%);
    -webkit-background-clip: text; background-clip: text; color: transparent;
  }
  .benefit-band {
    position: absolute; left: 0; top: 147px; width: 690px; height: 49px;
    background: linear-gradient(90deg, var(--brand-green-dark), var(--brand-green));
    clip-path: polygon(0 0, 100% 0, 96.5% 100%, 0 100%);
    display: flex; align-items: center;
    color: var(--white); font-size: 20.5px; font-weight: 600;
  }
  .benefit { display: flex; align-items: center; position: absolute; }
  .benefit svg { margin-right: 12px; }
  .benefit-same-day { left: 24px; }
  .benefit-locations { left: 352px; }
  .contact-strip {
    position: absolute; left: 0; top: 196px; width: 1000px; height: 96px;
  }
  .brand-name {
    position: absolute; left: 42px; top: 34px;
    display: flex; align-items: center;
    color: var(--brand-green); font-size: 19px; font-weight: 600;
  }
  .brand-dot {
    width: 18px; height: 18px; border-radius: 50%;
    background: var(--orange-deep); margin-right: 8px;
  }
  .phone-icon { position: absolute; left: 270px; top: 18px; }
  .phone-number {
    position: absolute; left: 340px; top: 6px;
    font-size: 64px; font-weight: 700; color: var(--ink);
    letter-spacing: -1.5px; white-space: nowrap; line-height: 1.2;
  }
  .divider {
    position: absolute; left: 830px; top: 20px; width: 2px; height: 50px;
    background: var(--brand-green);
  }
  .spanish-note {
    position: absolute; left: 852px; top: 16px; width: 108px;
    text-align: center; color: var(--ink);
    font-size: 21px; font-weight: 700; line-height: 1.3;
  }
</style>
</head>
<body>
  <section class="billboard">
    <div class="headline-panel"></div>
    <div class="portrait-area" role="img" aria-label="Smiling chiropractor in a dark blazer beside a glowing illustrated spine"></div>

    <h1 class="headline">
      <span class="headline-lead">Injured in a</span>
      <span class="headline-main">Car Accident?</span>
    </h1>

    <div class="benefit-band">
      <div class="benefit benefit-same-day">
        <svg width="24" height="24" viewBox="0 0 24 24" aria-hidden="true">
          <rect x="2" y="4" width="17" height="17" rx="2" fill="none" stroke="#111" stroke-width="2.4"/>
          <path d="M6 12l4 4 11-11" fill="none" stroke="#111" stroke-width="2.8" stroke-linecap="round" stroke-linejoin="round"/>
        </svg>
        Same Day Appointments
      </div>
      <div class="benefit benefit-locations">
        <svg width="22" height="28" viewBox="0 0 22 28" aria-hidden="true">
          <path d="M11 2a8 8 0 0 0-8 8c0 6 8 13 8 13s8-7 8-13a8 8 0 0 0-8-8z" fill="#111"/>
          <circle cx="11" cy="10" r="3" fill="#3e9140"/>
          <ellipse cx="11" cy="25" rx="9" ry="2.2" fill="none" stroke="#111" stroke-width="2"/>
        </svg>
        Locations across Georgia
      </div>
    </div>

    <div class="contact-strip">
      <div class="brand-name"><span class="brand-dot"></span>Kestrelwood Rehab</div>

      <svg class="phone-icon" width="52" height="52" viewBox="0 0 52 52" aria-hidden="true">
        <path d="M14 6c2-1 4 0 5 2l4 8c1 2 0 4-1 5l-3 3c2 5 6 9 11 11l3-3c1-1 3-2 5-1l8 4c2 1 3 3 2 5l-2 5c-1 2-3 3-5 3C22 47 5 30 5 12c0-2 1-4 3-5z" fill="#3e9140"/>
        <path d="M29 14a10 10 0 0 1 9 9" fill="none" stroke="#3e9140" stroke-width="3.5" stroke-linecap="round"/>
        <path d="M30 5a19 19 0 0 1 17 17" fill="none" stroke="#3e9140" stroke-width="3.5" stroke-linecap="round"/>
      </svg>
      <div class="phone-number">(770) 48-SPINE</div>

      <div class="divider"></div>
      <div class="spanish-note">HABLA<br>ESPANOL</div>
    </div>
  </section>
</body>
</html>
```